Design needed for Cover of Conference Brochure

We are a conference company that puts on several business conferences per year. We are putting together a new conference - the Clearpath Forum Week, and our audience is UX practitioners and specialists, product designers, UX designers, etc.
We need a brochure cover created. We are looking for fresh design ideas and are open to varying color schemes - please just keep in mind that this is a conference for business professionals, and fonts and colors should reflect this. Only restriction is that we do have a general cover format that we follow - i.e. which text goes where. (I've attached samples from our other events to reference.) We also generally have a central image to each brochure - feel free to submit a few versions with different images... we want something that accurately represents UX. However, if the design is compelling enough, image might not be completely necessary. We are relatively flexible - we just want something sharp!
- Must include BWKT logo (see placing on sample event covers)
- Must include footer - see sample covers
- Red text in word document are notes to you the designer - not actual text meant to appear on the cover
This cover is standard 8x11, and will be used for web only, not print. I have attached a word doc that includes all of the text that you will need for the cover. We will need final version in PDF, jpeg, and PSD. Please message me with any questions or clarification.

```html
<!DOCTYPE html>
<html lang="en">
<head>
<meta charset="utf-8">
<title>Clearpath Forum Week — Brochure Cover</title>
<link href="https://fonts.googleapis.com/css2?family=Archivo+Black&family=Michroma&family=Roboto:wght@400;700;900&display=swap" rel="stylesheet">
<style>
  :root {
    --royal: #1a1fd0;
    --royal-deep: #0a0f7a;
    --navy: #0d1270;
    --sky: #9fd6ff;
    --sky-pale: #e8f6ff;
    --head-blue: #2a8cf0;
    --head-glow: #6fd2ff;
    --sun: #ffe800;
    --amber: #ffb000;
    --tangerine: #ff8a00;
    --ink: #000000;
    --charcoal: #4a4a4a;
    --white: #ffffff;
    --bullet-blue: #1b1fb8;
  }
  * { box-sizing: border-box; margin: 0; padding: 0; }
  html, body { width: 873px; height: 1200px; overflow: hidden; }
  body { font-family: "Roboto", Arial, sans-serif; }

  .cover {
    position: relative;
    width: 873px;
    height: 1200px;
    overflow: hidden;
    background: radial-gradient(ellipse at 30% 45%, var(--sky-pale) 0%, #c9ebff 45%, var(--sky) 100%);
  }

  /* Masthead */
  .masthead {
    position: absolute;
    left: 15px; top: -6px;
    width: 847px; height: 488px;
    border: 5px solid #1a1a1a;
    border-radius: 0 0 14px 14px;
    background: radial-gradient(ellipse at 50% 35%, #2d35ff 0%, var(--royal) 45%, var(--royal-deep) 100%);
    overflow: hidden;
  }
  .masthead-title {
    position: absolute;
    left: 0; right: 0; top: 30px;
    text-align: center;
    font-family: "Archivo Black", "Arial Black", sans-serif;
    font-size: 158px;
    line-height: 0.98;
    letter-spacing: -1px;
    color: var(--white);
    text-shadow: 6px 8px 10px rgba(0,0,20,0.6);
  }
  .masthead-title .line { display: block; }
  .masthead-subtitle {
    position: absolute;
    left: 0; right: 0; top: 380px;
    text-align: center;
    font-family: "Michroma", sans-serif;
    font-size: 46px;
    letter-spacing: 3px;
    background: linear-gradient(180deg, #fffbd0 0%, var(--sun) 45%, var(--amber) 100%);
    -webkit-background-clip: text;
    background-clip: text;
    color: transparent;
  }
  .tagline-band {
    position: absolute;
    left: 0; right: 0; bottom: 0;
    height: 36px;
    background: var(--ink);
    color: var(--white);
    font-family: "Roboto", sans-serif;
    font-weight: 900;
    font-size: 17.5px;
    letter-spacing: 2.6px;
    line-height: 36px;
    text-align: center;
    white-space: nowrap;
  }

  /* Date panel */
  .date-panel {
    position: absolute;
    left: 20px; top: 498px;
    width: 332px; height: 64px;
    background: linear-gradient(180deg, #2a30c8 0%, var(--navy) 100%);
    border-radius: 0 4px 4px 0;
    padding: 10px 0 0 14px;
    box-shadow: 3px 4px 6px rgba(0,0,60,0.35);
  }
  .date-panel .dates {
    font-family: "Archivo Black", "Arial Black", sans-serif;
    font-size: 27px;
    line-height: 1;
    color: var(--sun);
    letter-spacing: 0.5px;
  }
  .date-panel .venue {
    margin-top: 5px;
    font-size: 8.5px;
    font-weight: 700;
    color: var(--sun);
    letter-spacing: 0.3px;
  }

  /* Central illustration */
  .hero-art {
    position: absolute;
    left: 20px; top: 560px;
    width: 620px; height: 528px;
    border-radius: 48% 40% 0 0 / 55% 45% 0 0;
    background: radial-gradient(ellipse at 45% 40%, var(--head-glow) 0%, var(--head-blue) 55%, #1a6fe0 100%);
    opacity: 0.9;
  }
  .hero-mark {
    position: absolute;
    left: 150px; top: 780px;
    font-family: "Roboto", sans-serif;
    font-weight: 900;
    font-size: 90px;
    color: #49d8ff;
    display: flex;
    align-items: center;
    gap: 16px;
  }
  .hero-mark .dot {
    width: 28px; height: 28px;
    border-radius: 50%;
    background: #49d8ff;
  }

  /* Highlights panel */
  .highlights {
    position: absolute;
    left: 541px; top: 565px;
    width: 332px; height: 435px;
    background: linear-gradient(160deg, var(--amber) 0%, var(--sun) 45%, #ffd000 70%, var(--tangerine) 100%);
    border-radius: 6px 0 0 6px;
    padding: 26px 22px 0 14px;
    box-shadow: -3px 4px 8px rgba(0,0,60,0.3);
  }
  .highlights ul { list-style: none; }
  .highlights li {
    font-family: "Roboto", sans-serif;
    font-weight: 900;
    font-size: 18.5px;
    line-height: 22.5px;
    letter-spacing: 0.9px;
    color: var(--bullet-blue);
    margin-bottom: 20px;
    text-transform: uppercase;
  }
  .highlights li::before { content: "• "; }

  /* Footer */
  .footer {
    position: absolute;
    left: 0; top: 1090px;
    width: 873px; height: 110px;
    background: linear-gradient(180deg, #555 0%, var(--charcoal) 100%);
  }
  .early-bird {
    position: absolute;
    left: 0; top: 0;
    width: 382px; height: 110px;
    background: linear-gradient(180deg, var(--tangerine) 0%, var(--amber) 45%, var(--sun) 100%);
    border-radius: 0 40px 0 0;
    padding: 8px 0 0 28px;
  }
  .early-bird .deadline {
    font-size: 21px;
    font-weight: 400;
    color: var(--ink);
    white-space: nowrap;
  }
  .early-bird .saving {
    font-family: "Archivo Black", "Arial Black", sans-serif;
    font-size: 46px;
    line-height: 1;
    color: var(--ink);
    margin-top: 4px;
    margin-left: -10px;
    white-space: nowrap;
  }
  .early-bird .saving .amp { font-size: 30px; vertical-align: 6px; }
  .register {
    position: absolute;
    left: 382px; right: 0; top: 0;
    text-align: center;
    padding-top: 14px;
  }
  .register .cta {
    font-family: "Archivo Black", "Arial Black", sans-serif;
    font-size: 41px;
    line-height: 1;
    letter-spacing: 1.5px;
    color: var(--sun);
    white-space: nowrap;
  }
  .register .contact {
    margin-top: 12px;
    font-weight: 700;
    font-size: 15.5px;
    color: var(--white);
    letter-spacing: 0.4px;
    white-space: nowrap;
  }
</style>
</head>
<body>
<main class="cover">

  <header class="masthead">
    <h1 class="masthead-title"><span class="line">CLEAR</span><span class="line">PATH</span></h1>
    <p class="masthead-subtitle">FORUM WEEK</p>
    <p class="tagline-band">DESIGN COMPELLING EXPERIENCES THROUGH SUCCESSFUL UX STRATEGY</p>
  </header>

  <section class="date-panel">
    <p class="dates">JUNE 10-12, 2014</p>
    <p class="venue">HARBOR POINT CLUB &amp; HOTEL, SAN FRANCISCO, CA</p>
  </section>

  <div class="hero-art" role="img" aria-label="Glowing blue profile silhouette of a human head facing left, symbolising user-centred thinking"></div>
  <div class="hero-mark"><span class="dot"></span>BWKT</div>

  <section class="highlights">
    <ul>
      <li>Case studies from leading brands on executing an effective UX strategy</li>
      <li>Learn how UX-driven innovation can change your business</li>
      <li>Build a successful UX team that operates strategically</li>
      <li>Insights into UX research, user behavior, usability testing, lean UX, and more</li>
    </ul>
  </section>

  <footer class="footer">
    <div class="early-bird">
      <p class="deadline">REGISTER BY MARCH 7TH, 2014</p>
      <p class="saving"><span class="amp">&amp;</span>SAVE $400!</p>
    </div>
    <div class="register">
      <p class="cta">REGISTER TODAY!</p>
      <p class="contact">888.555.0142 • WWW.CLEARPATHFORUMWEEK.COM</p>
    </div>
  </footer>

</main>
</body>
</html>
```